Brintell's Business Card

I need some designs for a new business card including the new logo attached. An old example of our business card is also attached to show all the data that should be included on the new design.
**I added some more examples someone had mocked up**

Contact Information for Business Card

Should include all info on other examples uploaded.

```html
<!DOCTYPE html>
<html lang="en">
<head>
<meta charset="utf-8">
<title>Brintell's Business Card</title>
<link rel="stylesheet" href="https://fonts.googleapis.com/css2?family=Open+Sans:wght@400;600;700;800&display=swap">
<style>
  :root {
    --backdrop: #7a7879;
    --brand-blue: #0f6dbb;
    --brand-red: #e91c24;
    --card-white: #ffffff;
    --card-black: #1b1b1b;
    --text-white: #ffffff;
  }
  * { margin: 0; padding: 0; box-sizing: border-box; }
  html, body { width: 1047px; height: 1200px; overflow: hidden; }
  body {
    background: var(--backdrop);
    font-family: "Open Sans", sans-serif;
    position: relative;
  }
  .card {
    position: absolute;
    left: 156px;
    width: 743px;
    height: 425px;
    border-radius: 22px;
    overflow: hidden;
    box-shadow: 2px 4px 8px rgba(0,0,0,0.35);
  }
  .card-front { top: 120px; background: var(--card-white); }
  .card-back { top: 634px; background: var(--card-black); }

  .front-waves { position: absolute; inset: 0; width: 100%; height: 100%; }

  .brand-lockup {
    position: absolute;
    top: 70px;
    left: 0; right: 0;
    display: flex;
    justify-content: center;
    align-items: center;
    gap: 16px;
  }
  .brand-dot {
    width: 22px; height: 22px;
    border-radius: 50%;
    background: var(--brand-red);
  }
  .brand-name {
    font-weight: 700;
    font-size: 62px;
    line-height: 1;
    color: var(--brand-blue);
  }

  .person-name {
    position: absolute;
    top: 313px; left: 0; right: 0;
    text-align: center;
    font-weight: 700;
    font-size: 34px;
    color: var(--text-white);
  }
  .contact-line {
    position: absolute;
    top: 364px; left: 0; right: 0;
    text-align: center;
    font-weight: 700;
    font-size: 20px;
    color: var(--text-white);
    letter-spacing: 0.3px;
  }
  .contact-line .divider { margin: 0 10px 0 14px; font-weight: 400; }
  .contact-line .email { font-size: 19px; }

  .back-lockup {
    position: absolute;
    top: 128px; left: 0; right: 0;
    display: flex;
    justify-content: center;
    align-items: center;
    gap: 18px;
  }
  .back-lockup .brand-dot { width: 28px; height: 28px; }
  .back-lockup .brand-name { font-size: 66px; }

  .back-info {
    position: absolute;
    top: 306px; left: 0; right: 0;
    text-align: center;
  }
  .service-area {
    font-weight: 700;
    font-size: 22px;
    color: var(--brand-blue);
    letter-spacing: 0.6px;
    line-height: 30px;
  }
  .call-to-action {
    font-weight: 600;
    font-size: 17.5px;
    color: var(--brand-red);
    line-height: 24px;
  }
  .credentials {
    font-weight: 600;
    font-size: 20px;
    color: var(--text-white);
    line-height: 34px;
  }
</style>
</head>
<body>

<section class="card card-front">
  <svg class="front-waves" viewBox="0 0 743 425" preserveAspectRatio="none" aria-hidden="true">
    <path d="M0,170 C110,285 360,300 743,178 L743,425 L0,425 Z" fill="var(--brand-blue)"/>
    <path d="M0,164 C110,280 360,292 743,172 L743,186 C360,300 110,290 0,178 Z" fill="var(--card-white)"/>
    <path d="M4,172 C90,270 300,300 700,228 C420,288 160,290 4,172 Z" fill="var(--brand-red)"/>
    <path d="M120,245 C260,272 520,250 743,186 L743,192 C520,258 280,280 120,245 Z" fill="var(--card-white)"/>
  </svg>

  <div class="brand-lockup">
    <span class="brand-dot"></span>
    <span class="brand-name">BRINTELL'S</span>
  </div>

  <p class="person-name">DALE BRINTELL</p>
  <p class="contact-line">555.014.2290<span class="divider">|</span><span class="email">hvacbrintell@mailbox.com</span></p>
</section>

<section class="card card-back">
  <div class="back-lockup">
    <span class="brand-dot"></span>
    <span class="brand-name">BRINTELL'S</span>
  </div>

  <div class="back-info">
    <p class="service-area">SERVES MAPLE FALLS, IA &amp; SURROUNDING AREAS</p>
    <p class="call-to-action">CALL TODAY FOR ALL YOUR HVAC, REFRIGERATION &amp; PLUMBING NEEDS</p>
    <p class="credentials">LICENSED &amp; INSURED | FAMILY OWNED &amp; OPERATED</p>
  </div>
</section>

</body>
</html>
```